Create website for home automation - Control your lighting, fans, blinds etc remotely by smartphone

Plan for SHOPIFY Website - Willowbyte Dwelling
Company name: Willowbyte Dwelling
Company Slogan: Calm Rooms Every Day
Clean, Modern, Easy to Navigate, easy to maintain - not a lot of coding. We need flash technology but displaying simply what we do.
What we provide:
We will be offering wireless switch which can be added to iOS/Android App via WiFi, allowing users to remotely turn on/off connected lights, fans, security cameras, appliances, irrigation, humidifier separately from anywhere at any time.
Control your home away from home. No more wandering of your mind on those lights or appliances which you might have left switched on. No need to drive back home to check and switch them off. Save that energy, money and time just with a click of your phone no matter how far you are from home.
Replace your home electrical switches with smart switches. They retrofit existing electrical switches and allow you to make the transformation as needed.
Easy to use and intuitive app allows you to control your lights and devices just at a click. Set any kind of ambiance suiting your occasion.
Set scenes in smartphone app to group and operate your devices just at a button click. Same device can be included in more than one scene.
Collections and Products
Light Switches
Wall Plugs
Fan Switch
Pendants etc special lighting types.
Light Dimmers
Blind Controllers
Home Page:
Home page needs to telling customers what we do and how we do it in a few words to grab people.
Logo
Phone
Email
Support – Download instructions per product
Client login
Wholesale login
Promotional video to be on home screen - this is a short 1.5 - 2 min illustration introduction video to who we are and what we do - this is yet to be created)
Social media link - Facebook
Pages:
FAQ
About Us
Support/Shipping/Returns policy
Support/Installation
Blog posts
Product pages:
Description
Price
Space for where a video will be featured - how each product works/installation.
Reviews
Our competition:
http://www.qorvat.com.au
https://brindlegadgetry.com.au/2018/04/05/best-smart-light-switches-and-plugs/
https://www.zelpinatech.com
Attachments:
Logo
Product pics
Promotional video - if ready

```html
<!DOCTYPE html>
<html lang="en">
<head>
<meta charset="utf-8">
<title>FAQ – Willowbyte Dwelling</title>
<link href="https://fonts.googleapis.com/css2?family=Questrial&family=Open+Sans:wght@400;600&display=swap" rel="stylesheet">
<style>
:root{
  --ink:#1b1b1b;
  --text:#444;
  --brand:#1d5fae;
  --rule:#8a8a8a;
  --footer:#141414;
  --footer-text:#e8e8e8;
  --white:#fff;
}
*{margin:0;padding:0;box-sizing:border-box}
html,body{width:868px;height:1200px;overflow:hidden;background:var(--white)}
body{position:relative;font-family:'Open Sans',sans-serif;color:var(--text)}
.site-header{position:absolute;left:0;top:0;width:868px;height:108px;border-bottom:1px solid #cfcfcf}
.brand{position:absolute;left:60px;top:40px;display:flex;align-items:center;gap:8px}
.brand-mark{width:14px;height:14px;background:var(--brand)}
.brand-text{font-family:'Questrial',sans-serif;font-size:15px;color:var(--brand);line-height:1.1}
.brand-text small{display:block;font-size:9px;letter-spacing:.5px}
.main-nav{position:absolute;left:0;top:46px;width:868px;height:20px;font-family:'Questrial',sans-serif;font-size:14px;color:var(--ink)}
.main-nav span{position:absolute;top:0;white-space:nowrap}
.main-nav .active{color:var(--brand)}
.nav-icon{position:absolute}
.cart-badge{position:absolute;left:757px;top:42px;width:8px;height:8px;border-radius:50%;background:var(--brand);color:#fff;font-size:6px;text-align:center;line-height:8px}
.page-title{position:absolute;top:142px;width:868px;text-align:center;font-family:'Questrial',sans-serif;font-size:34px;color:var(--ink);font-weight:400}
.faq{position:absolute;left:89px;top:226px;width:691px}
.faq-item{border-bottom:1px solid var(--rule);position:relative}
.faq-q{font-family:'Questrial',sans-serif;font-size:16.5px;color:var(--ink);text-transform:uppercase;height:76px;line-height:76px;padding-left:1px}
.faq-item.open .faq-q{height:30px;line-height:30px}
.faq-toggle{position:absolute;right:0;top:30px}
.faq-item.open .faq-toggle{top:8px}
.faq-a{font-size:11.1px;line-height:21.5px;padding:10px 0 30px 1px}
.faq-a p+p{margin-top:9px}
.site-footer{position:absolute;left:0;top:953px;width:868px;height:247px;background:var(--footer);border-top:7px solid var(--brand);color:var(--footer-text)}
.f-col{position:absolute;top:52px;font-size:10px}
.f-col h3{font-family:'Open Sans',sans-serif;font-weight:400;font-size:12px;margin-bottom:14px;color:#fff}
.f-col li{list-style:none;line-height:17px}
.f-col li::before{content:"» ";}
.contact p{line-height:16px;margin-bottom:4px;padding-left:3px}
.social{display:flex;gap:10px;margin-top:14px}
.social span{width:18px;height:18px;background:#f2f2f2;border-radius:3px}
.footer-rule{position:absolute;left:62px;top:186px;width:740px;border-top:1px solid #2a2a2a}
.copyright{position:absolute;top:204px;width:868px;text-align:center;font-size:11px;padding-left:18px}
</style>
</head>
<body>
<header class="site-header">
  <div class="brand"><span class="brand-mark"></span><div class="brand-text">Willowbyte Dwelling<small>Calm Rooms Every Day</small></div></div>
  <nav class="main-nav">
    <span style="left:276px">Home</span>
    <span style="left:331px">About Us</span>
    <span style="left:409px">Products</span>
    <span style="left:483px">Support</span>
    <span style="left:554px">Blog</span>
    <span class="active" style="left:603px">FAQ</span>
    <span style="left:651px">Contact</span>
  </nav>
  <svg class="nav-icon" style="left:725px;top:50px" width="14" height="14" viewBox="0 0 14 14"><circle cx="5.5" cy="5.5" r="4" fill="none" stroke="#111" stroke-width="2"/><line x1="8.5" y1="8.5" x2="13" y2="13" stroke="#111" stroke-width="2.4"/></svg>
  <svg class="nav-icon" style="left:753px;top:49px" width="16" height="14" viewBox="0 0 16 14"><path d="M1 5h14l-2 8H3z" fill="#111"/><path d="M4 5l4-4 4 4" fill="none" stroke="#111" stroke-width="1.5"/></svg>
  <span class="cart-badge">1</span>
  <svg class="nav-icon" style="left:788px;top:50px" width="16" height="14" viewBox="0 0 16 14"><circle cx="8" cy="4" r="3.5" fill="#111"/><path d="M1 14c0-5 14-5 14 0z" fill="#111"/></svg>
</header>

<h1 class="page-title">FAQ</h1>

<section class="faq">
  <div class="faq-item open">
    <div class="faq-q">Why not just use an app?</div>
    <svg class="faq-toggle" width="15" height="4"><rect width="15" height="4" fill="#111"/></svg>
    <div class="faq-a">
      <p>It is a long established fact that a reader will be distracted by the readable content of a page when looking at its layout. The point of using Lorem Ipsum is that it has a more-or-less normal distribution of letters, as opposed to using 'Content here, content here', making it look like readable English. Many desktop publishing packages and web page editors now use Lorem Ipsum as their default model text, and a search for 'lorem ipsum' will uncover many web sites still in their infancy.</p>
      <p>The point of using Lorem Ipsum is that it has a more-or-less normal distribution of letters, as opposed to using 'Content here, content here', making it look like readable English. Many desktop publishing packages and web page editors now use Lorem Ipsum as their default model text, and a search for 'lorem ipsum' will uncover many web sites still in their infancy.</p>
    </div>
  </div>
  <div class="faq-item"><div class="faq-q">Why neque porro quisquam est qui dolorem ipsum ?</div><svg class="faq-toggle" width="14" height="14"><rect x="5" width="4" height="14" fill="#111"/><rect y="5" width="14" height="4" fill="#111"/></svg></div>
  <div class="faq-item"><div class="faq-q">What porro quisquam est qui dolorem ipsum?</div><svg class="faq-toggle" width="14" height="14"><rect x="5" width="4" height="14" fill="#111"/><rect y="5" width="14" height="4" fill="#111"/></svg></div>
  <div class="faq-item"><div class="faq-q">How quisquam est qui dolorem ipsum quia ?</div><svg class="faq-toggle" width="14" height="14"><rect x="5" width="4" height="14" fill="#111"/><rect y="5" width="14" height="4" fill="#111"/></svg></div>
  <div class="faq-item"><div class="faq-q">When porro quisquam est qui dolorem ipsum quia dolor ?</div><svg class="faq-toggle" width="14" height="14"><rect x="5" width="4" height="14" fill="#111"/><rect y="5" width="14" height="4" fill="#111"/></svg></div>
  <div class="faq-item"><div class="faq-q">What dolorem ipsum quia dolor sit amet ?</div><svg class="faq-toggle" width="14" height="14"><rect x="5" width="4" height="14" fill="#111"/><rect y="5" width="14" height="4" fill="#111"/></svg></div>
  <div class="faq-item" style="border-bottom:none"><div class="faq-q">Why neque porro quisquam est qui dolorem ?</div><svg class="faq-toggle" width="14" height="14"><rect x="5" width="4" height="14" fill="#111"/><rect y="5" width="14" height="4" fill="#111"/></svg></div>
</section>

<footer class="site-footer">
  <div class="f-col" style="left:66px"><h3>INFORMATION</h3><ul><li>Privacy Policy</li><li>Your Account</li><li>Advanced Search</li><li>Contact Us</li></ul></div>
  <div class="f-col" style="left:259px"><h3>LINKS</h3><ul><li>Home</li><li>About us</li><li>Products</li><li>Shop</li></ul></div>
  <div class="f-col contact" style="left:406px"><h3>CONTACT US</h3>
    <p>Address : 42-48 Tessaly - Marrowin Road,<br>Marrowin, Canada</p>
    <p>Phone :&nbsp; (03) 5550 2741,&nbsp; (04) 5550 6682</p>
    <p>Email : sales@willowbyte.com.au</p></div>
  <div class="f-col" style="left:669px;top:49px"><h3>FOLLOW US OUT THERE</h3><div class="social"><span></span><span></span><span></span><span></span></div></div>
  <div class="footer-rule"></div>
  <div class="copyright">Copyright © 2018. All Rights Reserved</div>
</footer>
</body>
</html>
```